Permanent Makeup Certificate for Lash Craft Institute Certified Artists

I need a beautifully designed certificate for my students who have successfully obtained my certification for Eyebrow Micropigmentation.

I have attached my sample certificate in InDesign format. This certificate is how I want the Certified Artist Certificate to read. My wording is extremely important for US Insurance reasons. I would like it to be in 11 x 17 inch format for USA printing.

I have also attached samples of certificates from other companies to give you an idea of how fancy I would like it to be. My company colors are pink and white, so I would like the dominant colors to be shades of pink and white. I like pink pastel combines with darker shades of pink and white. If the design calls for another color in addition to pink, that would also be great. I really like the colors in the Veluna Certificate.

I have attached a copy of my signature in .png

Target Market(s)

Beauty Industry

Industry/Entity Type

Artists

Font styles to use
Serif
Script

Colors
ffffff
f9d9e8
9bcb3c
cadf82
e667a6
e34297
eea4c8
b7a5cd

Requirements
Must have
• Wording exactly as I uploaded in InDesign file
Nice to have
• Beautiful images of female face, I am not sure if I like this idea. Just an experiement

```html
<!DOCTYPE html>
<html lang="en">
<head>
<meta charset="utf-8">
<title>Certificate of Excellence – Lash Craft Institute</title>
<link href="https://fonts.googleapis.com/css2?family=Lobster&family=Raleway:wght@400;600;700&display=swap" rel="stylesheet">
<style>
  :root {
    --white: #ffffff;
    --blush: #f9d9e8;
    --blush-soft: #fbe9f2;
    --pink: #e667a6;
    --magenta: #d4148f;
    --plum: #8b1a7e;
    --ink: #2f2a2e;
    --line: #8a8388;
    --skin-light: #f3d9cc;
    --skin-mid: #e8c1ad;
  }
  * { margin: 0; padding: 0; box-sizing: border-box; }
  html, body { width: 1200px; height: 797px; overflow: hidden; background: var(--white); }
  .canvas { position: relative; width: 1200px; height: 797px; background: var(--white); }
  .sheet {
    position: absolute; left: 29px; top: 29px; width: 1142px; height: 739px; overflow: hidden;
    background: radial-gradient(ellipse at 62% 42%, var(--white) 0%, var(--blush-soft) 55%, var(--blush) 100%);
  }
  .portrait {
    position: absolute; left: 0; top: 0; width: 420px; height: 739px;
    background: linear-gradient(90deg, var(--skin-mid) 0%, var(--skin-light) 55%, rgba(249,217,232,0) 100%);
  }
  .frame { position: absolute; left: 0; top: 0; }
  .content { position: absolute; left: 0; top: 0; width: 1142px; height: 739px; font-family: "Raleway", sans-serif; color: var(--ink); }
  .centered { position: absolute; left: 420px; width: 582px; text-align: center; }
  .brand-name {
    top: 170px; font-family: "Raleway", sans-serif; font-weight: 600;
    font-size: 30px; letter-spacing: 3px; color: var(--plum);
  }
  .brand-name .dot { display: inline-block; width: 10px; height: 10px; border-radius: 50%; background: var(--plum); vertical-align: middle; margin-right: 12px; }
  .title { top: 262px; font-family: "Lobster", cursive; font-size: 58px; color: var(--plum); line-height: 1; }
  .certify-intro { top: 328px; font-size: 13px; letter-spacing: 0.5px; }
  .statement { top: 433px; font-size: 17px; line-height: 23.5px; }
  .sign-block { position: absolute; text-align: center; font-size: 11.5px; }
  .sign-block .rule { border-top: 1px solid var(--line); margin-bottom: 14px; }
  .date-block { left: 385px; top: 581px; width: 205px; }
  .instructor-block { left: 771px; top: 581px; width: 206px; }
  .label { font-weight: 700; }
  .instructor-name { font-weight: 700; line-height: 15px; }
  .instructor-role { line-height: 15.5px; }
  .signature { position: absolute; left: 785px; top: 548px; width: 180px; height: 30px; background: linear-gradient(90deg, rgba(47,42,46,0.08), rgba(47,42,46,0.02)); border-radius: 4px; }
</style>
</head>
<body>
<div class="canvas">
  <div class="sheet">
    <div class="portrait" role="img" aria-label="Photograph of a woman's face in close-up, showing groomed eyebrows and soft makeup"></div>

    <svg class="frame" width="1142" height="739" viewBox="0 0 1142 739" aria-hidden="true">
      <g fill="none" stroke="var(--magenta)" stroke-width="1.2">
        <path d="M323 54 H1093 V673 H215"/>
        <path d="M323 69 H1078 V658 H215"/>
      </g>
      <g fill="var(--pink)" opacity="0.85">
        <rect x="323" y="57" width="756" height="9"/>
        <rect x="1081" y="57" width="9" height="613"/>
        <rect x="215" y="661" width="866" height="9"/>
      </g>
      <g fill="none" stroke="var(--magenta)" stroke-width="1.2">
        <rect x="1079" y="55" width="12" height="12"/>
        <rect x="1079" y="659" width="12" height="12"/>
      </g>
    </svg>

    <div class="content">
      <div class="centered brand-name"><span class="dot"></span>LASH CRAFT INSTITUTE</div>
      <h1 class="centered title">Certificate of Excellence</h1>
      <p class="centered certify-intro">THIS IS TO CERTIFY THAT</p>
      <p class="centered statement">
        Has successfully proven to be an<br>
        Artist of the Highest Standard in Eyebrow Micropigmentation<br>
        using the LASH CRAFT GLOBAL® Microblading Method
      </p>

      <div class="sign-block date-block">
        <div class="rule"></div>
        <div class="label">Date</div>
      </div>

      <div class="signature" role="img" aria-label="Handwritten signature of the master instructor"></div>
      <div class="sign-block instructor-block">
        <div class="rule"></div>
        <div class="instructor-name">Clara Mae Renwick</div>
        <div class="instructor-role">Master Instructor</div>
        <div class="instructor-role">Lash Craft Global®</div>
      </div>
    </div>
  </div>
</div>
</body>
</html>
```